My Brightmere Interiors llc fliers project

A flyer that will be direct mailed to customers. feel free to play with wording this is what i have now. I wlil include every service i offer in must haves and feel free to run a footer stating all my services
" My background, I'm Corvin Altabresh, I was born Into this business, Its what I know. So if your tired of waiting for weeks before your kitchen gets completed, as happens with other companies. If your tired of dealing with unreliable contractors deal with me. I'm so confident in my work, here are the numbers to previous customer. Mrs.Pettigrew-555-218-4093. Mr.Kowalczyk 555-730-1856. They will tell you I can provide you that dream kitchen and countertop installed, within a week. Mention this flyer to receive an additional 10% discoun
BrightMere Interiors llc
5810 amber fern CT
Larkton VA,20917
555-964-2071
hello@brightmere-mail.example"

Target Market(s)

high income household income looking to get interior work done,

Industry/Entity Type

Church

Font styles to use
Serif

Requirements
Must have
• granite and marble kitchen and bathroom fabrication and install
• any flooring, hardwood, marble, carpet, laminate, install
• Kitchen cabinet design and install
• Bathroom remodeling
Nice to have
• an easy to read flyer that will give customers the info to reach me and understand what they do, if I put to much then reduce it.

```html
<!DOCTYPE html>
<html lang="en">
<head>
<meta charset="utf-8">
<title>Brightmere Interiors llc – Mailer</title>
<link rel="stylesheet" href="https://fonts.googleapis.com/css2?family=Cinzel:wght@400;700&family=Oswald:wght@500;600&family=Crimson+Text:wght@400;600&display=swap">
<style>
  :root{
    --orange:#f08a12;
    --ink:#1d1d1d;
    --charcoal:#2b2b2b;
    --paper:#ffffff;
    --backdrop:#4a4a4a;
    --badge:#d42a1c;
    --wood-a:#8a4f22;
    --wood-b:#c98b4a;
    --wood-c:#e8c79a;
  }
  *{box-sizing:border-box;margin:0;padding:0}
  html,body{width:769px;height:1200px;overflow:hidden}
  body{background:var(--backdrop);position:relative;font-family:"Crimson Text",serif;color:var(--ink)}

  .card{position:absolute;left:55px;width:660px;background:var(--paper);overflow:hidden;box-shadow:0 6px 18px rgba(0,0,0,.45)}
  .card--front{top:28px;height:530px}
  .card--back{top:600px;height:565px}

  .photo{position:absolute}
  .photo--kitchen-top{left:240px;top:0;width:420px;height:290px;
    background:linear-gradient(160deg,var(--wood-c) 0%,var(--wood-b) 35%,var(--wood-a) 75%,#3b2412 100%)}
  .photo--kitchen-bottom{left:318px;top:285px;width:342px;height:245px;
    background:linear-gradient(200deg,#f1e6cf 0%,var(--wood-c) 40%,var(--wood-b) 80%,var(--wood-a) 100%)}
  .shapes{position:absolute;left:0;top:0}

  .brand{position:absolute;left:20px;top:20px;font-family:"Cinzel",serif;font-weight:700;color:var(--paper);font-size:22px;line-height:1.15;letter-spacing:.5px}

  .headline{position:absolute;left:28px;top:150px;width:340px;font-family:"Oswald",sans-serif;line-height:1.02}
  .headline .hl-orange{color:var(--orange);font-weight:600}
  .headline .hl-dark{color:var(--ink);font-weight:500}
  .hl-1{font-size:40px}
  .hl-2{font-size:21px}
  .hl-3{font-size:37px;margin-bottom:10px}
  .hl-4{font-size:46px}
  .hl-5{font-size:23px}
  .cta{position:absolute;left:28px;top:430px;font-family:"Cinzel",serif;line-height:1.05}
  .cta-lead{font-size:24px;color:var(--ink)}
  .cta-main{font-size:30px;color:var(--orange);font-weight:700}

  .section-tab{position:absolute;left:0;height:34px;width:300px;background:var(--orange);border-radius:0 17px 17px 0;
    font-family:"Cinzel",serif;font-weight:700;color:var(--paper);font-size:20px;line-height:34px;padding-left:22px;
    border-bottom:3px solid var(--ink)}
  .section-tab--about{top:18px}
  .section-tab--services{top:222px}
  .about-copy{position:absolute;left:22px;top:62px;width:616px;font-size:14.5px;line-height:1.38;text-align:justify;color:#333}

  .services{position:absolute;left:22px;top:268px;width:240px;list-style:none;font-size:14px;line-height:1.25;color:#333}
  .services li{position:relative;padding-left:16px;margin-bottom:9px}
  .services li::before{content:"";position:absolute;left:0;top:5px;width:8px;height:8px;background:var(--orange)}

  .photo--bath{left:290px;top:250px;width:200px;height:150px;
    background:linear-gradient(135deg,#f4efe6 0%,var(--wood-c) 45%,var(--wood-b) 100%)}
  .badge{position:absolute;left:430px;top:330px;width:104px;height:104px;border-radius:50%;background:var(--badge);
    border:4px solid var(--paper);color:var(--paper);text-align:center;font-family:"Oswald",sans-serif;box-shadow:0 2px 6px rgba(0,0,0,.3)}
  .badge-lead{display:block;font-size:11px;margin-top:14px;line-height:1.1}
  .badge-big{display:block;font-size:36px;font-weight:600;line-height:1}
  .badge-off{display:block;font-size:15px;line-height:1}

  .contact{position:absolute;left:26px;top:458px;width:250px;color:var(--paper);font-size:13.5px;line-height:1.3;font-style:normal}
  .contact .contact-name{display:flex;align-items:center;gap:6px}
  .contact .pin{width:8px;height:8px;border-radius:50%;background:var(--orange)}
</style>
</head>
<body>

<section class="card card--front" aria-label="Mailer front">
  <div class="photo photo--kitchen-top" role="img" aria-label="Photo of a finished wood-cabinet kitchen with granite island and pendant lights"></div>
  <div class="photo photo--kitchen-bottom" role="img" aria-label="Photo of a bright kitchen with light cabinets and stainless appliances"></div>
  <svg class="shapes" width="660" height="530" viewBox="0 0 660 530" aria-hidden="true">
    <path d="M0,0 L232,0 C242,140 410,232 660,258 L660,300 C480,290 360,300 330,380 L330,530 L0,530 Z" fill="var(--paper)"/>
    <path d="M232,0 L250,0 C260,130 420,215 660,238 L660,258 C410,232 242,140 232,0 Z" fill="var(--orange)"/>
    <path d="M250,0 L258,0 C268,125 428,208 660,230 L660,238 C420,215 260,130 250,0 Z" fill="var(--ink)"/>
    <path d="M330,530 L330,380 C360,300 480,290 660,300 L660,288 C470,278 338,294 318,380 L318,530 Z" fill="var(--ink)"/>
    <path d="M0,0 H232 C233,40 235,70 240,95 C150,112 60,102 0,122 Z" fill="var(--orange)"/>
    <path d="M0,122 C60,102 150,112 240,95 L244,108 C150,124 60,117 0,137 Z" fill="var(--ink)"/>
  </svg>
  <div class="brand">BRIGHTMERE<br>INTERIORS LLC</div>
  <div class="headline">
    <div class="hl-1 hl-orange">Tired of waiting</div>
    <div class="hl-2 hl-dark">for weeks before your kitchen</div>
    <div class="hl-3 hl-orange">GETS COMPLETED?</div>
    <div class="hl-4 hl-orange">Tired of dealing</div>
    <div class="hl-5 hl-dark">with unreliable contractors?</div>
  </div>
  <div class="cta">
    <div class="cta-lead">Call me for a</div>
    <div class="cta-main">DREAM KITCHEN</div>
  </div>
</section>

<section class="card card--back" aria-label="Mailer back">
  <svg class="shapes" width="660" height="565" viewBox="0 0 660 565" aria-hidden="true">
    <path d="M0,430 C90,425 200,440 300,565 L0,565 Z" fill="var(--charcoal)"/>
    <path d="M0,420 C95,414 210,432 318,565 L300,565 C200,440 90,425 0,430 Z" fill="var(--orange)"/>
    <path d="M660,460 C560,470 470,510 430,565 L660,565 Z" fill="var(--orange)"/>
    <path d="M660,448 C555,458 462,502 418,565 L430,565 C470,510 560,470 660,460 Z" fill="var(--ink)"/>
    <circle cx="290" cy="325" r="30" fill="var(--orange)"/>
  </svg>

  <div class="section-tab section-tab--about">About Us</div>
  <p class="about-copy">My father opened a carpet store in Larkton in 1987 and introduced me to fabricating and installing granite, as well as designing and installing custom kitchen cabinets. I was born into this business and it is what I know. My careful approach and attention to detail make sure every job is done right the first time. If you are tired of waiting weeks for your kitchen, or tired of dealing with unreliable contractors, deal with me. Call Mrs.Pettigrew at 555-218-4093 or Mr.Kowalczyk at 555-730-1856 and they will tell you I can deliver that dream kitchen and countertop within a week. Mention this flyer for an extra discount.</p>

  <div class="section-tab section-tab--services">Services</div>
  <ul class="services">
    <li>Granite and marble kitchen and bathroom fabrication and install</li>
    <li>Any flooring: hardwood, marble, carpet, laminate, install</li>
    <li>Kitchen cabinet design and install</li>
    <li>Bathroom remodeling</li>
  </ul>

  <div class="photo photo--bath" role="img" aria-label="Photo of a remodeled kitchen corner with cabinets and countertop"></div>
  <div class="badge">
    <span class="badge-lead">Mention this flyer</span>
    <span class="badge-big">10%</span>
    <span class="badge-off">OFF</span>
  </div>

  <address class="contact">
    <div class="contact-name"><span class="pin"></span>BrightMere Interiors llc</div>
    <div>5810 amber fern CT</div>
    <div>Larkton VA,20917</div>
    <div>555-964-2071</div>
    <div>hello@brightmere-mail.example</div>
  </address>
</section>

</body>
</html>
```